Business Card Design

we need a bussiness card for the transport company called Varlen Transport
name of contact person that should display on card is Marek Tolleson contact no 0481620357
we do the dry goods and frozen deliveries in melbourne every day
happy to beat any quote

Industry/Entity Type

Business

Contact Information for Business Card

Varlen transport
Marek tolleson
mob 0481620357
contact us for any refrigerator or dry goods delivery
deliver all over melbourne

```html
<!DOCTYPE html>
<html lang="en">
<head>
<meta charset="utf-8">
<title>Varlen Transport – Business Card</title>
<link href="https://fonts.googleapis.com/css2?family=Questrial&family=Roboto+Condensed:wght@400;500&display=swap" rel="stylesheet">
<style>
  :root {
    --brand-red: #93231e;
    --brand-red-soft: #a5342d;
    --card-white: #f6f7f7;
    --card-white-low: #eceeee;
    --page: #ffffff;
    --text-light: #ffffff;
  }
  * { margin: 0; padding: 0; box-sizing: border-box; }
  html, body {
    width: 1095px;
    height: 1200px;
    overflow: hidden;
    background: var(--page);
    font-family: "Questrial", "Century Gothic", sans-serif;
  }
  .canvas { position: relative; width: 1095px; height: 1200px; }

  .card {
    position: absolute;
    width: 391px;
    height: 633px;
    box-shadow: 6px 6px 6px rgba(0,0,0,0.45);
    overflow: hidden;
  }

  /* Front */
  .card-front {
    left: 108px; top: 16px;
    background: linear-gradient(180deg, var(--page) 0%, var(--card-white) 55%, var(--card-white-low) 100%);
    color: var(--brand-red);
  }
  .side-stripe {
    position: absolute; left: 0; top: 0;
    width: 26px; height: 100%;
    background: var(--brand-red);
  }
  .stripe-gap {
    position: absolute; left: 0;
    width: 26px; height: 7px;
    background: var(--card-white);
  }
  .stripe-gap.first { top: 385px; }
  .stripe-gap.second { top: 465px; }

  .brand-mark {
    position: absolute;
    left: 45px; right: 20px; top: 92px; height: 216px;
    display: flex; align-items: center; justify-content: center; gap: 14px;
    color: var(--brand-red);
    font-size: 26px;
    letter-spacing: 1px;
  }
  .brand-mark .mark-dot {
    width: 22px; height: 22px; border-radius: 50%;
    background: var(--brand-red);
  }

  .front-title {
    position: absolute; left: 26px; right: 0;
    text-align: center;
    font-weight: 400;
    line-height: 1;
  }
  .front-title.primary { top: 338px; font-size: 66px; letter-spacing: 1px; }
  .front-title.secondary { top: 432px; font-size: 45px; letter-spacing: 1px; }

  .contact {
    position: absolute; right: 28px;
    text-align: right;
    line-height: 1;
  }
  .card-front .contact-name { top: 554px; font-size: 21px; letter-spacing: 1px; }
  .card-front .contact-phone { top: 589px; font-size: 16px; letter-spacing: 1.5px; }

  /* Back */
  .card-back {
    left: 618px; top: 526px;
    background: var(--brand-red);
    color: var(--text-light);
  }
  .back-watermark {
    position: absolute;
    left: 20px; right: 0; top: 150px;
    text-align: center;
    font-size: 58px;
    line-height: 1.1;
    color: var(--brand-red-soft);
  }
  .back-heading {
    position: absolute; left: 0; right: 0; top: 81px;
    text-align: center;
    font-size: 20px; letter-spacing: 1.5px;
  }
  .service-list {
    position: absolute; left: 0; right: 0; top: 199px;
    list-style: none;
    text-align: center;
    font-size: 20px; letter-spacing: 1px;
    line-height: 34px;
  }
  .delivery-banner {
    position: absolute; left: 0; right: 0; top: 388px;
    text-align: center;
    font-family: "Roboto Condensed", "Arial Narrow", sans-serif;
    font-weight: 500;
    font-size: 19px;
  }
  .card-back .contact-name { top: 509px; font-size: 22px; letter-spacing: 1px; }
  .card-back .contact-phone { top: 543px; font-size: 16px; letter-spacing: 1.5px; }
  .card-back .contact-email { top: 572px; font-size: 16px; letter-spacing: 0.3px; }
</style>
</head>
<body>
<main class="canvas">

  <section class="card card-front" aria-label="Business card front">
    <div class="side-stripe"></div>
    <div class="stripe-gap first"></div>
    <div class="stripe-gap second"></div>

    <div class="brand-mark">
      <span class="mark-dot"></span>
      <span class="mark-name">Varlen Transport</span>
    </div>

    <h1 class="front-title primary">VARLEN</h1>
    <h2 class="front-title secondary">TRANSPORT</h2>

    <p class="contact contact-name">Marek Tolleson</p>
    <p class="contact contact-phone">mob 0481620357</p>
  </section>

  <section class="card card-back" aria-label="Business card back">
    <div class="back-watermark" aria-hidden="true">Varlen<br>Transport</div>

    <p class="back-heading">VARLEN TRANSPORT</p>

    <ul class="service-list">
      <li>Contact Us</li>
      <li>For Any Refrigerator</li>
      <li>Or Dry Goods Delivery</li>
      <li>Deliver All Over Melbourne</li>
    </ul>

    <p class="delivery-banner">WE DELIVER AROUND MELBOURNE EVERYDAY!</p>

    <p class="contact contact-name">Marek Tolleson</p>
    <p class="contact contact-phone">mob 0481620357</p>
    <p class="contact contact-email">marek@varlentransport.com</p>
  </section>

</main>
</body>
</html>
```